Business Card Design for Funky New Cloud Security Start-up

We're looking for kick ass business cards to make use stand out from the crowd in a world that's dominated by dull, boring, blue logos.

We have a logo (designed here on pixel forum) and we'd like to build on the brand theme of "Security made simple."

Please use following details for sample:

Martin Colby
CEO
+61 (0)4077 518 206
mart@quenvo.com

2714/58 Harwood Street
Sydney NSW 2000
Australia

Target Market(s)

Customers will be large enterprise clients - typically VP level. Also resellers of our product who are mid-tier.

Industry/Entity Type

Business

Font styles to use
Sans Serif

Requirements
Must have
• Use the colour scheme from the attached logo
Do not put space for a fax - it's old school
Easy to use on nova press
Use a font that complements the logo font

```html
<!DOCTYPE html>
<html lang="en">
<head>
<meta charset="utf-8">
<title>Quenvo Business Cards</title>
<link rel="stylesheet" href="https://fonts.googleapis.com/css2?family=Quicksand:wght@400;500&family=Questrial&display=swap">
<style>
  :root {
    --backdrop: #0b0b0b;
    --brand-blue-dark: #235670;
    --brand-blue: #2678a0;
    --brand-green: #b3d445;
    --ink-grey: #5b5c5f;
    --ink-navy: #2a4f70;
    --paper: #ffffff;
  }
  * { margin: 0; padding: 0; box-sizing: border-box; }
  html, body {
    width: 1200px; height: 1200px; overflow: hidden;
    background: var(--backdrop);
  }
  .stage { position: relative; width: 1200px; height: 1200px; }

  .card-front {
    position: absolute; left: 70px; top: 80px;
    width: 720px; height: 400px;
    background: linear-gradient(135deg, var(--brand-blue-dark) 0%, var(--brand-blue) 45%, var(--brand-blue-dark) 100%);
    display: flex; flex-direction: column; align-items: center; justify-content: center;
    color: var(--paper);
  }
  .brand-lockup { display: flex; align-items: center; gap: 22px; }
  .brand-dot { width: 56px; height: 56px; border-radius: 50%; background: var(--paper); }
  .brand-name {
    font-family: "Quicksand", sans-serif; font-weight: 500;
    font-size: 118px; line-height: 1; letter-spacing: 1px;
  }
  .tagline {
    margin-top: 18px;
    font-family: "Quicksand", sans-serif; font-weight: 400;
    font-size: 34px; letter-spacing: 1px;
  }

  .card-profile {
    position: absolute; left: 634px; top: 460px;
    width: 400px; height: 700px;
    background: var(--paper); overflow: hidden;
  }
  .card-profile .bands { position: absolute; inset: 0; }
  .holder { position: absolute; left: 42px; top: 72px; }
  .holder-name {
    font-family: "Quicksand", sans-serif; font-weight: 500;
    font-size: 38px; color: var(--brand-green); letter-spacing: 1px;
    text-transform: uppercase; line-height: 1.1;
  }
  .holder-role {
    font-family: "Questrial", sans-serif;
    font-size: 32px; color: var(--paper); margin-top: 8px;
  }
  .profile-lockup {
    position: absolute; left: 28px; top: 300px;
    display: flex; align-items: center; gap: 16px;
  }
  .profile-lockup .brand-dot { width: 40px; height: 40px; background: var(--brand-blue); }
  .profile-lockup .brand-name { font-size: 80px; color: var(--ink-grey); }

  .contact {
    position: absolute; left: 30px; top: 510px;
    list-style: none;
    font-family: "Questrial", sans-serif; color: var(--ink-navy);
    font-size: 23px; letter-spacing: 1px; line-height: 1.15;
  }
  .contact li { display: flex; align-items: flex-start; gap: 12px; margin-bottom: 8px; }
  .contact svg { width: 26px; height: 26px; flex: none; fill: var(--ink-navy); margin-top: 1px; }
</style>
</head>
<body>
<main class="stage">

  <section class="card-front">
    <div class="brand-lockup">
      <span class="brand-dot"></span>
      <span class="brand-name">quenvo.</span>
    </div>
    <p class="tagline">security made simple</p>
  </section>

  <section class="card-profile">
    <svg class="bands" viewBox="0 0 400 700" preserveAspectRatio="none">
      <defs>
        <linearGradient id="band-blue" x1="0" y1="0" x2="1" y2="1">
          <stop offset="0" stop-color="#235670"/>
          <stop offset="0.5" stop-color="#2678a0"/>
          <stop offset="1" stop-color="#235670"/>
        </linearGradient>
      </defs>
      <polygon points="0,0 400,0 400,180 0,265" fill="url(#band-blue)"/>
      <polygon points="0,478 400,392 400,700 0,700" fill="#b3d445"/>
    </svg>

    <div class="holder">
      <p class="holder-name">Martin Colby</p>
      <p class="holder-role">CEO</p>
    </div>

    <div class="profile-lockup">
      <span class="brand-dot"></span>
      <span class="brand-name">quenvo.</span>
    </div>

    <ul class="contact">
      <li>
        <svg viewBox="0 0 24 24"><path d="M6.6 3.2l2.6 3.4-1.6 2.2c1 2.4 3 4.5 5.6 5.7l2.2-1.6 3.4 2.6-1.3 3c-7.6-.4-13.2-6-13.9-13.9z"/></svg>
        <span>+61 (0)4077 518 206</span>
      </li>
      <li>
        <svg viewBox="0 0 24 24"><path d="M2 6h20v13H2z M2 6l10 7 10-7" fill="none" stroke="#2a4f70" stroke-width="2"/><path d="M2 6h20l-10 7z"/></svg>
        <span>mart@quenvo.com</span>
      </li>
      <li>
        <svg viewBox="0 0 24 24"><path d="M12 3l10 9h-3v9h-5v-6h-4v6H5v-9H2z"/></svg>
        <span>2714/58 Harwood Street<br>Sydney NSW 2000 Australia</span>
      </li>
    </ul>
  </section>

</main>
</body>
</html>
```